Design our Security Warning Sticker to deter thefts and promote our business

Warning sticker to be a deterrent on our customer sites but also do a little advertising for our services at the same time

Create a STANDOUT DESIGN design that will be a deterrent but it will also be promotional for our business services.

We are looking for something that will be bright using our colours as attached. It will not be the same as all other security warning signs but it will be a great design that will demand attention and be easily read without having to much rubbish writing. Should easy to see and the number and website should be clear to see. We may use our website www.guardlyne.co.nz

Target Market(s)

Commercial, Government, residential

Industry/Entity Type

Security

Requirements
Must have
• WARNING
• PROTECTED BY (or something like this)
• LOGO
• 0800 457 216
• ALARMS, ACCESS CONTROL, CCTV, INTERCOMS, DATA CABLING
Nice to have
• Website: www.vantorix.co

```html
<!DOCTYPE html>
<html lang="en">
<head>
<meta charset="utf-8">
<title>Vantorix Security Warning Stickers</title>
<link rel="stylesheet" href="https://fonts.googleapis.com/css2?family=Saira:wght@500;600;700&display=swap">
<style>
  :root {
    --backdrop: #3a3a3a;
    --red: #e2342a;
    --red-dark: #c42a22;
    --black: #1c1a1b;
    --smoke-left: #242223;
    --smoke-right: #3b393a;
    --white: #ffffff;
    --light-grey: #ececec;
    --navy: #114a7a;
  }
  * { margin: 0; padding: 0; box-sizing: border-box; }
  html, body { width: 1200px; height: 901px; overflow: hidden; }
  body {
    background: var(--backdrop);
    position: relative;
    font-family: "Saira", sans-serif;
  }
  .sticker {
    position: absolute;
    top: 131px;
    width: 311px;
    height: 636px;
    border-radius: 15px;
    overflow: hidden;
    text-align: center;
    color: var(--white);
  }
  .sticker--black { left: 87px; background: var(--black); }
  .sticker--smoke {
    left: 445px;
    background: linear-gradient(90deg, var(--smoke-left) 0 50%, var(--smoke-right) 50% 100%);
  }
  .sticker--white { left: 805px; background: var(--white); color: var(--navy); }

  .sticker__warning {
    position: absolute; top: 24px; left: 0; right: 0;
    font-weight: 700; font-size: 50px; line-height: 1;
    letter-spacing: 1px; color: var(--red);
  }
  .sticker__protected {
    position: absolute; top: 89px; left: 0; right: 0;
    font-weight: 600; font-size: 13px; letter-spacing: 0.5px;
  }
  .sticker__brand {
    position: absolute; top: 108px; left: 0; right: 0;
    font-weight: 600; font-size: 38px; line-height: 1; letter-spacing: 1.5px;
    color: var(--light-grey);
  }
  .sticker--white .sticker__brand { color: var(--navy); }
  .sticker__tagline {
    position: absolute; top: 146px; left: 0; right: 0;
    font-weight: 500; font-size: 9.5px; letter-spacing: 2px; color: var(--red);
    white-space: nowrap;
  }
  .sticker__mark {
    position: absolute; top: 210px; left: 50%;
    width: 250px; height: 250px; margin-left: -125px;
    border-radius: 50%; background: var(--red);
  }
  .sticker--smoke .sticker__mark { background: var(--red-dark); }
  .sticker__phone {
    position: absolute; top: 500px; left: 0; right: 0;
    font-weight: 600; font-size: 38px; line-height: 1; color: var(--red);
    letter-spacing: 0.5px;
  }
  .sticker__services {
    position: absolute; top: 546px; left: 0; right: 0;
    font-weight: 700; font-size: 13.5px; line-height: 19px;
    white-space: nowrap;
  }
  .sticker__band {
    position: absolute; bottom: 0; left: 0; right: 0; height: 38px;
    background: var(--red); color: var(--white);
    font-weight: 600; font-size: 14px; line-height: 38px;
  }
</style>
</head>
<body>
  <article class="sticker sticker--black">
    <h1 class="sticker__warning">WARNING</h1>
    <p class="sticker__protected">PROTECTED BY</p>
    <p class="sticker__brand">VANTORIX</p>
    <p class="sticker__tagline">ALWAYS WATCHING, ALWAYS READY</p>
    <div class="sticker__mark" aria-hidden="true"></div>
    <p class="sticker__phone">0800 457 216</p>
    <p class="sticker__services">ALARMS, ACCESS CONTROL, CCTV<br>INTERCOMS, DATA CABLING</p>
    <p class="sticker__band">www.vantorix.co</p>
  </article>

  <article class="sticker sticker--smoke">
    <h1 class="sticker__warning">WARNING</h1>
    <p class="sticker__protected">PROTECTED BY</p>
    <p class="sticker__brand">VANTORIX</p>
    <p class="sticker__tagline">ALWAYS WATCHING, ALWAYS READY</p>
    <div class="sticker__mark" aria-hidden="true"></div>
    <p class="sticker__phone">0800 457 216</p>
    <p class="sticker__services">ALARMS, ACCESS CONTROL, CCTV<br>INTERCOMS, DATA CABLING</p>
    <p class="sticker__band">www.vantorix.co</p>
  </article>

  <article class="sticker sticker--white">
    <h1 class="sticker__warning">WARNING</h1>
    <p class="sticker__protected">PROTECTED BY</p>
    <p class="sticker__brand">VANTORIX</p>
    <p class="sticker__tagline">ALWAYS WATCHING, ALWAYS READY</p>
    <div class="sticker__mark" aria-hidden="true"></div>
    <p class="sticker__phone">0800 457 216</p>
    <p class="sticker__services">ALARMS, ACCESS CONTROL, CCTV<br>INTERCOMS, DATA CABLING</p>
    <p class="sticker__band">www.vantorix.co</p>
  </article>
</body>
</html>
```